Printing company needs website!

A printing company would like a new professional website (made with wix). Now they don't have a website, but they want a unique, beautiful, clear site. Of course they provide the content themselves, we are now looking for the beautiful design with some mockups. You can see several of their projects on their instagram & facebook.
Www.pagenook.com/velmoor and https://www.snapfolio.com/velmoor.be/ logos are attached.

```html
<!DOCTYPE html>
<html lang="en">
<head>
<meta charset="utf-8">
<title>Velmoor — Printing</title>
<link href="https://fonts.googleapis.com/css2?family=Montserrat:wght@400;500;600;700;800&family=Lato:wght@400;700&display=swap" rel="stylesheet">
<style>
:root{
  --teal:#43bfa9;
  --blue:#0ea7d6;
  --navy:#1e3f8d;
  --ink:#1b1b1b;
  --text:#333;
  --muted:#555;
  --footer:#232323;
  --line:#bdbdbd;
}
*{box-sizing:border-box;margin:0;padding:0}
html,body{width:1200px;height:3673px;overflow:hidden}
body{position:relative;font-family:'Lato',sans-serif;color:var(--text);background:#fff}
.abs{position:absolute}
h2{font-family:'Montserrat',sans-serif;font-weight:700;color:var(--ink);font-size:24px;text-align:center}
.rule{width:56px;height:3px;background:var(--navy);margin:14px auto 0}
.btn{display:inline-block;background:var(--teal);color:#fff;font-family:'Montserrat',sans-serif;font-weight:700;text-transform:uppercase;text-align:center}

/* header */
.header{top:0;left:0;width:1200px;height:71px;background:#fff}
.brand{left:130px;top:16px;display:flex;align-items:center;gap:10px;font-family:'Montserrat',sans-serif;font-weight:700;font-size:30px;color:#2b2b2b}
.brand-dot{width:34px;height:34px;border-radius:50%;background:var(--teal)}
.nav{right:134px;top:26px;display:flex;gap:40px;font-family:'Montserrat',sans-serif;font-size:13px;font-weight:500;color:#222}
.nav .on{color:var(--teal);text-decoration:underline}

/* hero */
.hero{top:71px;left:0;width:1200px;height:509px;background:linear-gradient(90deg,#5c3a20,#7a4e2c 30%,#6a4224 60%,#55351c)}
.hero-box{left:117px;top:69px;width:533px;height:350px;background:linear-gradient(180deg,#c9a57a 0%,#c9a57a 50%,#3a8bb8 72%,#1f4e86 100%);box-shadow:0 10px 25px rgba(0,0,0,.35)}
.hero-title{left:694px;top:118px;font-family:'Montserrat',sans-serif;font-weight:800;font-size:38px;color:#fff}
.hero-text{left:695px;top:182px;width:370px;font-size:17.5px;line-height:21px;color:#fff}
.hero-btn{left:695px;top:314px;width:118px;height:37px;line-height:37px;font-size:14px}
.arrow{top:236px}

/* products */
.products{top:580px;left:0;width:1200px;height:570px}
.products h2{margin-top:28px}
.prod{top:100px;width:302px;text-align:center}
.prod-img{height:276px;background:linear-gradient(180deg,#ececec,#d9d9d9)}
.prod h3{font-family:'Montserrat',sans-serif;font-weight:500;font-size:15px;margin-top:29px;color:#111}
.prod p{font-size:13px;line-height:18px;margin:16px 12px 0;color:#333}
.prod .btn{margin-top:16px;width:93px;height:28px;line-height:28px;font-size:11px}

/* about */
.about{top:1150px;left:0;width:1200px;height:493px;background:var(--blue)}
.about-img{left:0;top:0;width:591px;height:493px;background:linear-gradient(135deg,#6d6d6d,#b9b9b9 45%,#c64b4b 70%,#8a8a8a)}
.about-title{left:658px;top:48px;font-family:'Montserrat',sans-serif;font-weight:700;font-size:26px;color:#fff}
.about-rule{left:658px;top:96px;width:88px;height:2px;background:#fff}
.about-text{left:658px;top:140px;width:410px;font-size:15.5px;line-height:24px;color:#fff}
.about-btn{left:658px;top:393px;width:124px;height:39px;line-height:39px;background:#fff;color:var(--blue);font-size:15px}

/* why */
.why{top:1643px;left:0;width:1200px;height:378px}
.why h2{margin-top:48px}
.why-item{top:138px;width:280px;text-align:center}
.why-item h3{font-family:'Montserrat',sans-serif;font-weight:500;font-size:20px;color:#111;margin-top:14px}
.why-item p{font-size:13px;line-height:20px;margin-top:14px;color:#333}

/* testimonials */
.testi{top:2021px;left:0;width:1200px;height:433px;background:var(--blue)}
.testi h2{color:#fff;margin-top:44px;font-size:26px}
.testi .rule{background:var(--navy)}
.quote{top:140px;width:280px;text-align:center;color:#fff}
.quote .mark{font-family:'Montserrat',sans-serif;font-weight:800;font-size:44px;line-height:40px}
.quote p{font-size:13.5px;line-height:17.5px;margin-top:18px}
.quote .who{position:absolute;top:262px;left:0;width:280px;font-weight:700;font-size:13px}

/* blog */
.blog{top:2454px;left:0;width:1200px;height:586px;background:#f2f2f2}
.blog h2{margin-top:38px}
.post{top:122px;width:302px;height:409px;background:#fff}
.post-img{height:189px}
.post h3{font-family:'Montserrat',sans-serif;font-weight:600;font-size:14px;line-height:19px;color:#111;margin:28px 24px 0}
.post p{font-size:12px;line-height:16.5px;color:#444;margin:18px 24px 0}
.post .btn{margin:22px 0 0 24px;width:80px;height:23px;line-height:23px;font-size:9.5px}

/* contact */
.contact{top:3040px;left:0;width:1200px;height:548px}
.contact h2{margin-top:46px}
.map{left:130px;top:126px;width:534px;height:240px;background:linear-gradient(135deg,#eef0ec,#e2e6df 60%,#bcd9ee)}
.addr{left:130px;top:392px;font-size:14px;line-height:25.5px;color:#222}
.field{left:710px;width:356px;border:1px solid #a9a9a9;font-family:'Montserrat',sans-serif;font-size:12px;color:#444;padding:16px 16px 0}
.submit{left:710px;top:450px;width:356px;height:46px;line-height:46px;font-size:16px}

/* footer */
.footer{top:3588px;left:0;width:1200px;height:85px;background:var(--footer)}
.copy{left:127px;top:34px;font-size:14px;color:#fff}
.social{top:22px;width:40px;height:40px;border:1.5px solid #fff;border-radius:50%;background:#111;color:#fff;font-family:'Montserrat',sans-serif;font-weight:600;font-size:11px;text-align:center;line-height:37px}
</style>
</head>
<body>

<header class="abs header">
  <div class="abs brand"><span class="brand-dot"></span>Velmoor</div>
  <nav class="abs nav">
    <span class="on">HOME</span><span>ABOUT US</span><span>SERVICES</span><span>BLOG</span><span>TESTIMONIALS</span><span>CONTACT US</span>
  </nav>
</header>

<section class="abs hero">
  <div class="abs hero-box" role="img" aria-label="Printed kraft mailer box mockup with an illustrated seafood design"></div>
  <svg class="abs arrow" style="left:38px" width="22" height="36" viewBox="0 0 22 36"><path d="M18 3 4 18l14 15" fill="none" stroke="#fff" stroke-width="4"/></svg>
  <svg class="abs arrow" style="left:1136px" width="22" height="36" viewBox="0 0 22 36"><path d="M4 3l14 15L4 33" fill="none" stroke="#fff" stroke-width="4"/></svg>
  <div class="abs hero-title">BOX PRINTING</div>
  <p class="abs hero-text">There are many variations of passages of Lorem Ipsum available, but the majority have suffered alteration in some form, by injected humour, or randomised words which don't look even slightly believable</p>
  <span class="abs btn hero-btn">READ MORE</span>
</section>

<section class="abs products">
  <h2>OUR PRODUCTS</h2><div class="rule"></div>
  <div class="abs prod" style="left:130px">
    <div class="prod-img" role="img" aria-label="Floral patterned product box mockup" style="background:linear-gradient(180deg,#eef0ee,#d8dcd6)"></div>
    <h3>LOREM IPSUM</h3>
    <p>There are many variations of passages of Lorem Ipsum available, but the majority have suffered alteration in some form, by injected.</p>
    <span class="btn">READ MORE</span>
  </div>
  <div class="abs prod" style="left:453px">
    <div class="prod-img" role="img" aria-label="Supplement bottle with purple label mockup" style="background:linear-gradient(180deg,#efeff2,#dcdce2)"></div>
    <h3>LOREM IPSUM</h3>
    <p>There are many variations of passages of Lorem Ipsum available, but the majority have suffered alteration in some form, by injected.</p>
    <span class="btn">READ MORE</span>
  </div>
  <div class="abs prod" style="left:770px">
    <div class="prod-img" role="img" aria-label="Kraft coffee pouch mockup" style="background:linear-gradient(180deg,#ececec,#d6d2cc)"></div>
    <h3>LOREM IPSUM</h3>
    <p>There are many variations of passages of Lorem Ipsum available, but the majority have suffered alteration in some form, by injected.</p>
    <span class="btn">READ MORE</span>
  </div>
</section>

<section class="abs about">
  <div class="abs about-img" role="img" aria-label="Printing press rollers running printed material"></div>
  <div class="abs about-title">ABOUT US</div>
  <div class="abs about-rule"></div>
  <p class="abs about-text">There are many variations of passages of Lorem Ipsum available, but the majority have suffered alteration in some form, by injected humour, or randomised words which don't look even slightly believable. If you are going to use a passage of Lorem Ipsum, you need to be sure there isn't anything embarrassing hidden in the middle of text.All the Lorem Ipsum generators on the Internet tend to repeat predefined chunks as necessary, making this the first true generator on the Internet.</p>
  <span class="abs btn about-btn">READ MORE</span>
</section>

<section class="abs why">
  <h2>WHY CHOOSE US</h2><div class="rule"></div>
  <div class="abs why-item" style="left:107px">
    <svg width="70" height="72" viewBox="0 0 70 72" fill="none" stroke="#1aa3d9" stroke-width="2.5"><rect x="8" y="8" width="40" height="56" rx="3"/><rect x="20" y="3" width="16" height="9" rx="2"/><path d="M14 24h4M14 34h4M14 44h4M24 24h16M24 34h14M24 44h10"/><circle cx="48" cy="50" r="10"/><path d="M55 57l9 9"/></svg>
    <h3>Flexible and Fast</h3>
    <p>Lorem Ipsum is simply dummy text of the printing and typesetting industry. Lor em Ipsum has been the industry'.</p>
  </div>
  <div class="abs why-item" style="left:458px">
    <svg width="64" height="70" viewBox="0 0 64 70" fill="none" stroke="#1aa3d9" stroke-width="2.5"><path d="M32 4 58 14v22c0 16-12 26-26 31C18 62 6 52 6 36V14z"/><path d="M22 34h6v16h-6zM28 48h14c2 0 4-2 4-4l2-8c0-2-1-4-3-4h-9l2-8c0-3-4-4-5-1l-5 9"/></svg>
    <h3>Graphics support</h3>
    <p>Lorem Ipsum is simply dummy text of the printing and typesetting industry. Lor em Ipsum has been the industry'.</p>
  </div>
  <div class="abs why-item" style="left:800px">
    <svg width="66" height="66" viewBox="0 0 66 66" fill="none" stroke="#1aa3d9" stroke-width="2.5"><path d="M33 12l6 13 14 2-10 10 3 14-13-7-13 7 3-14-10-10 14-2z"/><path d="M33 2v5M60 22l-5 2M6 22l5 2M50 60l-3-4M16 60l3-4"/></svg>
    <h3>Own Placement Service</h3>
    <p>Lorem Ipsum is simply dummy text of the printing and typesetting industry. Lor em Ipsum has been the industry'.</p>
  </div>
</section>

<section class="abs testi">
  <h2>CUSTOMER TESTIMONIALS</h2><div class="rule"></div>
  <div class="abs quote" style="left:121px">
    <div class="mark">&ldquo;</div>
    <p>It is a long established fact that a reader will be distracted by the readable content of a page when looking at its layout. The point of using Lorem Ipsum is that it has a more-or-less normal distribution of letters, as opposed to using 'Content here, content here', making it look likereadable English. Many desktop publishing packages and web  lorem ipsum.</p>
    <div class="who">Riverton City, CA</div>
  </div>
  <div class="abs quote" style="left:460px">
    <div class="mark">&ldquo;</div>
    <p style="margin-top:26px">Lorem Ipsum is simply dummy text of the printing and typesetting industry. Lorem Ipsum has been the industry's standard dummy text ever since the 1500s, when an unknown printer took a galley of type and scrambled it to make a type specimen book. It has survived not only five centuries,</p>
    <div class="who">Ashford Hills, CA</div>
  </div>
  <div class="abs quote" style="left:795px">
    <div class="mark">&ldquo;</div>
    <p style="margin-top:26px">Contrary to popular belief, Lorem Ipsum is not simply random text. It has roots in a piece of classical Latin literature from 45 BC, making it over 2000 years old. Edwin Marlowe, a Latin professor at Thornbury College in Virginia, looked up one of the more obscure Latin words, consectetur, from .</p>
    <div class="who">Marcus Delane, Investor</div>
  </div>
</section>

<section class="abs blog">
  <h2>LATEST BLOG</h2><div class="rule"></div>
  <article class="abs post" style="left:130px">
    <div class="post-img" role="img" aria-label="Branded stationery set on a desk" style="background:linear-gradient(135deg,#dfe6e4,#c9a883 55%,#b9d6cf)"></div>
    <h3>At vero eos et accusamus et iusto odio dignissimos</h3>
    <p>On the other hand, we denounce with righte ous indignation and dislike men who are so beguiled and demoralized by the charms of pleasure of the moment,</p>
    <span class="btn">READ MORE</span>
  </article>
  <article class="abs post" style="left:449px">
    <div class="post-img" role="img" aria-label="Printed flag with company branding" style="background:linear-gradient(135deg,#6fbfa5,#f2f2f2 55%,#6fbfa5)"></div>
    <h3>At vero eos et accusamus et iusto odio dignissimos</h3>
    <p>On the other hand, we denounce with righte ous indignation and dislike men who are so beguiled and demoralized by the charms of pleasure of the moment,</p>
    <span class="btn">READ MORE</span>
  </article>
  <article class="abs post" style="left:765px">
    <div class="post-img" role="img" aria-label="Printing machine with red and green rollers" style="background:linear-gradient(135deg,#4a4a4a,#c23b3b 50%,#5bbf4a)"></div>
    <h3>At vero eos et accusamus et iusto odio dignissimos</h3>
    <p>On the other hand, we denounce with righte ous indignation and dislike men who are so beguiled and demoralized by the charms of pleasure of the moment,</p>
    <span class="btn">READ MORE</span>
  </article>
</section>

<section class="abs contact">
  <h2>CONTACT US</h2><div class="rule"></div>
  <div class="abs map" role="img" aria-label="Street map showing the office location"></div>
  <div class="abs addr">27 Harlow Quay Street, Fenmoor, CA 90412<br>Email: info@velmoor.be<br>Tel: +32 400 00 12 34</div>
  <div class="abs field" style="top:126px;height:48px">NAME</div>
  <div class="abs field" style="top:189px;height:47px">EMAIL</div>
  <div class="abs field" style="top:252px;height:47px">PHONE</div>
  <div class="abs field" style="top:314px;height:115px">MESSAGE</div>
  <span class="abs btn submit">SUBMIT</span>
</section>

<footer class="abs footer">
  <div class="abs copy">Copyright © 2022 All Rights Reserved</div>
  <div class="abs social" style="left:969px" aria-label="Pagenook">PN</div>
  <div class="abs social" style="left:1024px" aria-label="Snapfolio">SF</div>
</footer>

</body>
</html>
```